Automotive eCommerce Business looking for a business card design

Looking for a clean and simple business card design. Our company name is "Harbor Crest Auto" and we are a company specializing in the ecommerce sales of automotive parts, specifically for pick up trucks and large SUVs. Our company colours are red, black, and white.

Feel free to use the logo provided or create a new logo that you seem fit. Looking forward to your creative ideas!

Industry/Entity Type

Automotive

Contact Information for Business Card

We were thinking of a possibly two-sided design featuring just the logo and company name on one side, and personal information on the other side. Single sided designs will be considered as well.

Font styles to use
Serif
Sans Serif
Decorative

Colors
ec1f27
ffffff
000000

Requirements
Must have
• Space for employee's name, title, phone number and email address, along with the company address and website somewhere.

```html
<!DOCTYPE html>
<html lang="en">
<head>
<meta charset="UTF-8">
<title>Harbor Crest Auto Ltd – Business Cards</title>
<link href="https://fonts.googleapis.com/css2?family=Montserrat:wght@400;500;600&display=swap" rel="stylesheet">
<style>
  :root {
    --brand-red: #ec1f27;
    --brand-white: #ffffff;
    --brand-black: #000000;
    --card-black: #070707;
    --stage: #2b2b2b;
    --muted: #d9d9d9;
  }
  * { margin: 0; padding: 0; box-sizing: border-box; }
  html, body { width: 1200px; height: 930px; overflow: hidden; }
  body {
    background: var(--stage);
    font-family: "Montserrat", sans-serif;
    position: relative;
  }
  .card {
    position: absolute;
    width: 560px;
    height: 320px;
    border-radius: 16px;
    background: linear-gradient(135deg, var(--card-black) 0%, #151515 55%, var(--card-black) 100%);
    overflow: hidden;
    color: var(--brand-white);
  }
  .card-front { left: 110px; top: 110px; }
  .card-back { left: 530px; top: 490px; }

  .brand-lockup {
    display: flex;
    align-items: center;
    gap: 10px;
    font-weight: 600;
    color: var(--brand-white);
    white-space: nowrap;
  }
  .brand-dot {
    width: 14px; height: 14px;
    border-radius: 50%;
    background: var(--brand-red);
    flex: none;
  }
  .card-front .brand-lockup {
    position: absolute;
    left: 0; right: 0; top: 118px;
    justify-content: center;
    font-size: 34px;
  }
  .front-website {
    position: absolute;
    left: 0; right: 0; top: 250px;
    text-align: center;
    font-size: 14px;
    color: var(--brand-white);
  }
  .domain { color: var(--brand-red); }

  .card-back .brand-lockup {
    position: absolute;
    left: 30px; top: 122px;
    font-size: 18px;
    gap: 8px;
  }
  .card-back .brand-dot { width: 12px; height: 12px; }
  .divider {
    position: absolute;
    left: 282px; top: 50px;
    width: 1px; height: 120px;
    background: var(--brand-red);
  }
  .contact-block {
    position: absolute;
    left: 304px; top: 42px;
  }
  .person-name {
    color: var(--brand-red);
    font-size: 20px;
    font-weight: 500;
    letter-spacing: 0.5px;
    text-transform: uppercase;
  }
  .person-title {
    font-size: 13px;
    color: var(--muted);
    margin-top: 2px;
    margin-bottom: 12px;
  }
  .contact-list { list-style: none; }
  .contact-list li {
    display: flex;
    align-items: center;
    gap: 9px;
    font-size: 12.5px;
    line-height: 20px;
    color: var(--brand-white);
    white-space: nowrap;
  }
  .contact-list svg { width: 11px; height: 11px; flex: none; fill: var(--brand-red); }
  .back-wave { position: absolute; left: 0; top: 0; width: 560px; height: 320px; }
</style>
</head>
<body>

  <section class="card card-front" aria-label="Business card front">
    <div class="brand-lockup"><span class="brand-dot"></span>Harbor Crest Auto Ltd</div>
    <p class="front-website">www.<span class="domain">harborcrestautoltd</span>.com</p>
  </section>

  <section class="card card-back" aria-label="Business card back">
    <svg class="back-wave" viewBox="0 0 560 320" aria-hidden="true">
      <path d="M0,266 C150,282 300,264 410,216 C470,190 525,178 560,176 L560,320 L0,320 Z" fill="var(--brand-red)"/>
      <path d="M0,280 C150,296 305,278 415,228 C475,201 527,190 560,188 L560,194 C527,196 478,207 420,234 C308,286 150,304 0,288 Z" fill="var(--brand-white)"/>
      <path d="M0,296 C110,308 220,304 330,282 C230,310 120,320 0,320 Z" fill="var(--brand-white)"/>
    </svg>

    <div class="brand-lockup"><span class="brand-dot"></span>Harbor Crest Auto Ltd</div>
    <div class="divider"></div>

    <div class="contact-block">
      <h1 class="person-name">Daniel Marsh</h1>
      <p class="person-title">Director</p>
      <ul class="contact-list">
        <li>
          <svg viewBox="0 0 24 24"><path d="M6.6 10.8a15 15 0 0 0 6.6 6.6l2.2-2.2a1 1 0 0 1 1-.25 11.4 11.4 0 0 0 3.6.57 1 1 0 0 1 1 1V20a1 1 0 0 1-1 1A17 17 0 0 1 3 4a1 1 0 0 1 1-1h3.5a1 1 0 0 1 1 1c0 1.250.2 2.45.57 3.57a1 1 0 0 1-.25 1z"/></svg>
          <span>555.201.4410</span>
        </li>
        <li>
          <svg viewBox="0 0 24 24"><path d="M7 1h10a2 2 0 0 1 2 2v18a2 2 0 0 1-2 2H7a2 2 0 0 1-2-2V3a2 2 0 0 1 2-2zm0 3v14h10V4zm5 15.5a1 1 0 1 0 0 2 1 1 0 0 0 0-2z"/></svg>
          <span>555.318.7702</span>
        </li>
        <li>
          <svg viewBox="0 0 24 24"><path d="M2 5h20v14H2zm2 2v.5l8 5 8-5V7zm0 2.8V17h16V9.8l-8 5z"/></svg>
          <span>info@harborcrestautoltd.com</span>
        </li>
        <li>
          <svg viewBox="0 0 24 24"><path d="M12 2a10 10 0 1 0 0 20 10 10 0 0 0 0-20zm6.9 6h-2.9a15.6 15.6 0 0 0-1.4-3.6A8 8 0 0 1 18.9 8zM12 4c.8 1.2 1.5 2.5 1.9 4h-3.8c.4-1.5 1.1-2.8 1.9-4zM4.3 14a8 8 0 0 1 0-4h3.4a16 16 0 0 0 0 4zm.8 2h2.9c.3 1.3.8 2.5 1.4 3.6A8 8 0 0 1 5.1 16zM8 8H5.1a8 8 0 0 1 4.3-3.6C8.8 5.5 8.3 6.7 8 8zm4 12c-.8-1.2-1.5-2.5-1.9-4h3.8c-.4 1.5-1.1 2.8-1.9 4zm2.3-6H9.7a14.6 14.6 0 0 1 0-4h4.6a14.6 14.6 0 0 1 0 4zm.3 5.6c.6-1.1 1.1-2.3 1.4-3.6h2.9a8 8 0 0 1-4.3 3.6zm1.7-5.6a16 16 0 0 0 0-4h3.4a8 8 0 0 1 0 4z"/></svg>
          <span>www.<span class="domain">harborcrestautoltd</span>.com</span>
        </li>
      </ul>
    </div>
  </section>

</body>
</html>
```